Telecoms and IT Technology Company Blue Van Wrap Livery Signage

We want to brand our vans with a design that stands out and is remembered.

Attached is our logo, I've also included the fonts if you want to use these although not necessary. All fonts used should look good together, for example a serif font wouldn't look good

The design will be used across 4 vans we have, they're white and small with the biggest being a Corvane Tessel and the smallest being a Valdrin Moppet. Please show examples using smaller vans

We'd like to show our services we offer, which include:
IT Support,
Telecoms and Internet,
Cloud Computing,
Cyber Security,
Network Design and Installation,
Printers and Copiers,

Our website address: www.brellonvex.co.uk
our telephone: 0330 418 7961
our slogan: Local IT Experts
I've included some samples of other vans we thought looked ok
we're not looking for a full van wrap to keep costs down, maximum 50% wrap

Target Market(s)

SME's within the North East England

Industry/Entity Type

Information Technology

Font styles to use
Sans Serif

Colors
33a6d7
0492cd
3176b5
ffffff

Requirements
Must have
• Logo and company colours
Should not have
• Full wrap

```html
<!DOCTYPE html>
<html lang="en">
<head>
<meta charset="utf-8">
<title>Brellonvex – Van Livery</title>
<link rel="stylesheet" href="https://fonts.googleapis.com/css2?family=Exo+2:wght@300;400;500&display=swap">
<style>
  :root {
    --bg: #8f9094;
    --bg-light: #a7a8ac;
    --white: #ffffff;
    --blue: #33a6d7;
    --blue-deep: #0492cd;
    --blue-dark: #3176b5;
    --trim: #2b2d30;
    --outline: #d9dde1;
  }
  html, body {
    margin: 0;
    padding: 0;
    width: 1200px;
    height: 674px;
    overflow: hidden;
  }
  body {
    background: radial-gradient(ellipse at 50% 40%, var(--bg-light), var(--bg));
    font-family: "Exo 2", Arial, sans-serif;
  }
  .livery { display: block; width: 1200px; height: 674px; }
  .panel-body { fill: var(--white); stroke: var(--outline); stroke-width: 1; }
  .wrap-blue { fill: var(--blue); }
  .wrap-blue-deep { fill: var(--blue-deep); }
  .trim-band { fill: var(--trim); }
  .brand-name { font-weight: 300; fill: var(--blue-dark); }
  .brand-slogan { font-weight: 300; fill: var(--blue-dark); letter-spacing: 1px; }
  .brand-mark { fill: var(--blue); }
  .rear .brand-name, .rear .brand-slogan { fill: var(--white); }
  .rear .brand-mark { fill: var(--white); }
  .service { font-size: 7px; fill: var(--blue-dark); }
  .service-dot { fill: var(--blue); }
  .contact-web { font-size: 9.5px; fill: var(--blue-dark); font-weight: 500; }
  .contact-phone { font-size: 12px; fill: var(--blue-dark); font-weight: 500; }
</style>
</head>
<body>
<svg class="livery" viewBox="0 0 1200 674" xmlns="http://www.w3.org/2000/svg">

  <!-- Near side elevation -->
  <g class="side side-near">
    <rect class="panel-body" x="120" y="85" width="520" height="215" rx="18"/>
    <polygon class="wrap-blue" points="462,85 640,85 640,300 520,300"/>
    <polygon class="wrap-blue-deep" points="560,85 640,85 640,300 600,300"/>
    <rect class="trim-band" x="120" y="255" width="520" height="14"/>

    <rect class="brand-mark" x="345" y="148" width="12" height="12"/>
    <text class="brand-name" x="362" y="160" font-size="26">Brellonvex</text>
    <text class="brand-slogan" x="345" y="187" font-size="14">local it experts</text>

    <g class="services">
      <circle class="service-dot" cx="347" cy="212" r="1.8"/><text class="service" x="352" y="214.5">IT Support</text>
      <circle class="service-dot" cx="347" cy="220" r="1.8"/><text class="service" x="352" y="222.5">Website Design</text>
      <circle class="service-dot" cx="347" cy="228" r="1.8"/><text class="service" x="352" y="230.5">Telecoms</text>
      <circle class="service-dot" cx="347" cy="236" r="1.8"/><text class="service" x="352" y="238.5">Printers and Copiers</text>
      <circle class="service-dot" cx="430" cy="212" r="1.8"/><text class="service" x="435" y="214.5">Networks</text>
      <text class="service" x="435" y="222.5">(wired/wireless)</text>
      <circle class="service-dot" cx="430" cy="228" r="1.8"/><text class="service" x="435" y="230.5">Cloud Services</text>
      <circle class="service-dot" cx="430" cy="236" r="1.8"/><text class="service" x="435" y="238.5">Cyber Security</text>
    </g>

    <text class="contact-web" x="197" y="225">www.brellonvex.co.uk</text>
    <text class="contact-phone" x="197" y="239">Call:0330 418 7961</text>
  </g>

  <!-- Off side elevation -->
  <g class="side side-off">
    <rect class="panel-body" x="125" y="352" width="565" height="212" rx="18"/>
    <polygon class="wrap-blue" points="125,352 300,352 225,564 125,564"/>
    <polygon class="wrap-blue-deep" points="125,352 180,352 150,564 125,564"/>
    <rect class="trim-band" x="125" y="520" width="565" height="14"/>
    <rect class="trim-band" x="153" y="459" width="138" height="5"/>

    <rect class="brand-mark" x="303" y="415" width="12" height="12"/>
    <text class="brand-name" x="320" y="427" font-size="26">Brellonvex</text>
    <text class="brand-slogan" x="303" y="454" font-size="14">local it experts</text>

    <g class="services">
      <circle class="service-dot" cx="303" cy="477" r="1.8"/><text class="service" x="308" y="479.5">IT Support</text>
      <circle class="service-dot" cx="303" cy="485" r="1.8"/><text class="service" x="308" y="487.5">Website Design</text>
      <circle class="service-dot" cx="303" cy="493" r="1.8"/><text class="service" x="308" y="495.5">Telecoms</text>
      <circle class="service-dot" cx="303" cy="501" r="1.8"/><text class="service" x="308" y="503.5">Printers and Copiers</text>
      <circle class="service-dot" cx="380" cy="477" r="1.8"/><text class="service" x="385" y="479.5">Networks</text>
      <text class="service" x="385" y="487.5">(wired/wireless)</text>
      <circle class="service-dot" cx="380" cy="493" r="1.8"/><text class="service" x="385" y="495.5">Cloud Services</text>
      <circle class="service-dot" cx="380" cy="501" r="1.8"/><text class="service" x="385" y="503.5">Cyber Security</text>
    </g>

    <text class="contact-web" x="480" y="489">www.brellonvex.co.uk</text>
    <text class="contact-phone" x="480" y="502">Call:0330 418 7961</text>
  </g>

  <!-- Rear doors -->
  <g class="rear">
    <rect class="wrap-blue" x="765" y="135" width="315" height="395" rx="22"/>
    <polygon class="wrap-blue-deep" points="765,300 1080,300 1080,530 765,530"/>
    <polygon class="panel-body" points="1080,310 1080,500 900,500" style="stroke:none"/>
    <line x1="922" y1="140" x2="922" y2="500" stroke="#2a8fc0" stroke-width="1"/>
    <rect class="trim-band" x="770" y="450" width="130" height="7" rx="2"/>
    <rect class="trim-band" x="765" y="500" width="315" height="30" rx="4"/>

    <rect class="brand-mark" x="800" y="198" width="18" height="18"/>
    <text class="brand-name" x="826" y="217" font-size="38">Brellonvex</text>
    <text class="brand-slogan" x="802" y="252" font-size="22">local it experts</text>
  </g>
</svg>
</body>
</html>
```